Quiz Dale Penrose (Page Forge or Flinket template)

Business Name?
Quiz Dale Penrose (QuizDalePenrose.com) Technically, this is the name of the web site. This is a venture, rather than a business. It is part of building my brand as an expert.

- What do you do?
I am a life strategist/coach (http://VelotrimGroup.example/). This site will be a one-stop advice site, providing answers to real life challenges. The tagline is "life challenges, real solutions." It is a three step process: ASK-RECEIVE-ACHIEVE. It should, however, be FUN/ENGAGING (yet useful), rather than have a business/consultant feel. Approachable!

- How many pages do you need designed and code?
The site will have 7 sections:
Home (this is where I envision the introductory text, the ability for the user to submit their questions and they will be visible for all to see)
About Dale (my bio information/fascinating facts)
Dale's Notes (my blog-discussing general personal development topics and comments from readers)
Audio/Video (video tips and an audio player from chatwaveaudio.example that enables visitors to listen to my radio show/podcast)
Donations (this is where visitors can donate after they have had their questions answered. I am not attached to a specific vendor as long as it is NOT CoinRelay-perhaps Zentra Pay. I need to have designated dollar increments that people can select-perhaps in $5 or $10 intervals)
Contact Dale (contact information and perhaps a VOXLY access button so that they can immediately contact me; it might be nice to have a chat room here for online chat, but I don't see this as vital)

- What is your industry?
Consulting/Professional Services

- Describe the target audience for your website design?
EVERYONE! I am going to becoming the "go-to guy" for when you are feeling stuck.

- What 3 things would you like to communicate to your audience through your website design?
Insightful, Engaging, Wise (& FUN, FUN, FUN!). This is not a traditional business site. I have one of those. It should be fun & cutting-edge.

- How is your company different from your competitors?
It is not what I do that is different. It is my approach. I believe that success is a product of conditioning. Rather than simply focusing on what you are doing (which is, naturally, important), you must also focus on who you are. "YOU" are the common denominator in all that you do!

- What website design styles do you like?
I tend to be attracted to fashion/photography/artist web sites. I love this Flinket Lidbox design:
http://skinbazaar.example/item/lidbox/full_screen_preview/7739205
I would love to have this style of menu navigation (these type of icons).

- What colors do you want to see in your website design?
I am completely open at this point (I have a couple of people working on a logo. It's not done yet. I now that it incorporates black & red, so, a black background might be nice). Naturally, this could influence it. I like "slick, sleek and cutting edge-something that will pop off the screen!

- What colors do you NOT want to see in your website design?
No restrictions as long as they are utilized in the appropriate balance/combination.

- What adjectives should best describe your website design?
Slick, sleek, cutting edge, cool, engaging, artistic

- What content must be included in the website design?
In addition to my logo and tagline : "life challenges, real solutions," I want to feature: ASK-RECEIVE-ACHIEVE somewhere.

- Do you have additional requirements or links you want to share?
The primary challenge (and unlike most web sites) is that the main section is user-driven. The user submits the questions and I respond after it is posted (unlike a typical blog where I post and users comment). In an ideal world I would like for the user to be able to select from one of six categories while submitting their question.(Relationships, Health/Body, Career/Work Life, Spirituality, Money/Finance, Other). Then, when the user selects their category, their question would be displayed in the appropriate section. The challenge with that is that I need to have at least some q&a displayed on the home page so that visitors get an immediate sense of what I am doing. I want to have the ability to also response to submitted questions via video should I choose to do so. I want visitors to be able to share postings/my responses on Chatterly, Peepline, etc.

Page Forge has 3 templates that enable this q&a capability, but they are very unattractive in their design (like tech help forums-EW!) and they seem to require users to create their own profile page, etc. I don't see that as necessary. I don't know what can be modified, turned off, etc.
http://toppfhelpdesk.example/the-best-pageforge-themes-for-creating-qa-websites/
Updates

First of all: Thank you for bringing your creative gifts/talents/expertise to my challenge!

I assume it is sometimes challenging having to fill space without the actual words, so I have attached some documents that I am hoping will be helpful.

Logo-I didn't know what type of file you need, so I have attached .jpg, .pns, .eps
Pictures-I will be having some professional pics taken, but in the interim, I have attached 3 that can be used. I like the one with the hat as the main pic.
Documents:
-Quiz Dale Penrose Home-this is the text for the introduction that precedes the Q&A section on the home page
-About Dale/25 Random Facts-for the About Dale section.
-Dale's Notes-I have attached some blog entries for this section

If you have any questions, please do not hesitate to contact me. Thanks, again, for joining me. Please know that I work without a great many people who are in need of good designers for their projects/businesses. I will happily direct them to the people with the best talents when we are through. I want this to be a win-win for all of us!

Hello Designers!

I wanted to take a moment to stress that I really want something "cutting-edge." I am NOT looking for something that is traditional (and especially not something that has a corporate/consultant flavor). I want FUN. As I have stated-think artist/fashion/creative. I referred you all to the Flinket design because I like that look at feel. I like the navigation icons and the navigation of that template. Because I like cutting edge, please refrain from the use of stock photography or clip art.

I really need for users to know immediately what this site is all about-right from the home page, without having to navigate around. I have always envisioned q&a being on the home page. If this cannot work, I am open to alternatives, as long as it is clear what the site is about. 

I attached the logo, the intro text and some text for other sections for a reason. Please use it! This will enable me to truly envision what you see and how this should all blend together. Thank you so much.

If I can provide any additional information or assistance, please do not hesitate to contact me. 

Hello Designers:

I had a slight modification made to the logo (a little more white space-think you'll like it better). I deleted the old files and uploaded new attachments of the revised logo. I wasn't sure which file format you prefer to work with so I included a few!

Please do not hesitate to ask any questions should they arise. Thanks for your hard work.

Dale

Reason: Since many seem to be pressed to participate due to competing schedules, I am adding a couple more days. Only a couple! Before submitting a design, please pay close attention to my brief. I must see how the home page intro and the q&a will be incorporated and displayed. To all who choose to contribute their gifts and talents to this challenge, I really appreciate it. Thanks! Dale

Target Market(s)

EVERYONE! Yes, the world!

Industry/Entity Type

Building

Requirements
Must have
• There can be no compromise in the user-driven question and answer capability (where the questions are clearly displayed for all to see). This is the point of the entire site, so without it, there is no point!

All have my desired sections have already been detailed above.
Should not have
• I do not want this site to look like a typical coaching or corporate consulting site. Fun, engaging, cutting edge & forward thinking!

```html
<!DOCTYPE html>
<html lang="en">
<head>
<meta charset="utf-8">
<title>Dale Penrose – questions answered</title>
<link rel="stylesheet" href="https://fonts.googleapis.com/css2?family=Source+Sans+3:ital,wght@0,400;0,600;0,700;1,400&display=swap">
<style>
:root{
  --page:#232323;
  --topbar:#161616;
  --band:#121212;
  --footer:#0c0c0c;
  --red:#e2463d;
  --green:#8fae2c;
  --blue:#3aa0c8;
  --text:#d6d6d6;
  --panel:#e6e6e6;
  --card:#d8d8d8;
  --card-edge:#f2f2f2;
  --ink:#2a2a2a;
  --btn-green:#7c9c22;
  --white:#ffffff;
}
*{box-sizing:border-box;margin:0;padding:0}
html,body{width:741px;height:1200px;overflow:hidden}
body{background:var(--page);font-family:"Source Sans 3",sans-serif;color:var(--text);position:relative}
.abs{position:absolute}

/* top bar */
.topbar{left:0;top:0;width:741px;height:33px;background:var(--topbar);border-bottom:1px solid #2e2e2e}
.social-signin{left:307px;top:9px;height:16px;width:95px;background:#4a6da8;border-radius:2px;color:var(--white);font-size:8px;display:flex;align-items:center;gap:4px;padding-left:4px}
.social-signin .sq{width:8px;height:8px;background:var(--white);opacity:.85}
.toplinks{left:414px;top:10px;font-size:10px;color:#ccc;display:flex;gap:8px}
.toplinks span.sep{color:#777}
.search{left:578px;top:8px;width:129px;height:17px;background:#f4f4f4;border-radius:2px;font-size:8px;font-style:italic;color:#aaa;padding:3px 8px}

/* header */
.brand-name{left:66px;top:66px;font-size:26px;font-weight:600;color:var(--text);line-height:1}
.mainnav{left:416px;top:60px;display:flex;gap:19px}
.mainnav svg{width:20px;height:20px;fill:#e6e6e6}

/* slider */
.band{left:0;top:137px;width:741px;height:180px;background:var(--band)}
.slider-frame{left:66px;top:128px;width:610px;height:196px;background:#3c3c3c;border:1px solid #555}
.slider{left:73px;top:135px;width:596px;height:181px;background:linear-gradient(#fafafa,#dcdcdc)}
.slider-art{left:144px;top:163px;width:222px;height:125px;background:linear-gradient(135deg,#cfcfcf,#9a9a9a);border-radius:4px}
.steps{left:403px;top:198px;display:flex;gap:28px;font-size:19px;font-weight:600}
.steps .ask{color:var(--red)}.steps .rec{color:var(--green)}.steps .ach{color:var(--blue)}
.dots{left:549px;top:287px;display:flex;gap:13px}
.dots i{width:9px;height:9px;border-radius:50%;background:#4a4a4a;display:block}
.dots i.on{background:#c0302a}
.arrow{top:212px;width:18px;height:28px}
.arrow path{stroke:#bbb;stroke-width:3;fill:none}

/* intro */
h2{font-size:16px;font-weight:600;color:var(--red)}
.intro{left:33px;top:348px;width:680px;font-size:9.8px;line-height:15.5px}
.intro p{margin-top:6px}
.intro ol{margin:2px 0 0 26px;list-style:none}
.intro .aside{margin:6px 0 0 26px}
.guarantee{color:#a6c43a;font-size:14px;margin-top:6px}
.portrait{left:465px;top:457px;width:119px;height:119px;border:2px solid #ccc;background:linear-gradient(135deg,#8a8a8a,#3a3a3a)}

/* question */
.q-title{left:34px;top:602px}
.q-panel{left:37px;top:628px;width:667px;height:96px;background:var(--panel);border-radius:4px}
.q-label{left:68px;top:638px;font-size:8px;font-style:italic;color:#666}
.q-select{left:59px;top:655px;width:113px;height:20px;background:#f8f8f8;border:1px solid #bbb;border-radius:2px;font-size:8px;font-style:italic;color:#777;padding:4px 8px}
.q-select svg{position:absolute;right:6px;top:7px;width:8px;height:5px;fill:#777}
.btn{height:18px;background:linear-gradient(#9cc034,var(--btn-green));border-radius:3px;color:var(--white);font-size:9px;font-weight:700;display:flex;align-items:center;justify-content:center;border:1px solid #62801a}
.q-divider{left:197px;top:638px;width:1px;height:76px;background:#c8c8c8}
.q-text{left:213px;top:641px;width:476px;height:70px;background:var(--white);border:1px solid #ccc;border-radius:3px;font-size:9px;font-style:italic;color:#999;padding:14px 13px}

/* categories */
.cat-head{display:flex;align-items:center;gap:12px}
.cat-icon{width:34px;height:30px;border-radius:4px}
.cat-head h3{font-size:16px;font-weight:600;color:var(--red)}
.card{width:213px;height:123px;background:linear-gradient(var(--card-edge),var(--card));border:2px solid #f5f5f5;padding:10px 12px;color:var(--ink)}
.card .lead{font-size:8.6px;font-weight:700;line-height:12px;text-align:justify}
.card .body{font-size:8.2px;font-style:italic;line-height:12.3px;margin-top:8px;text-align:justify;color:#333}
.viewall{width:72px;height:18px;background:#f2f2f2;border-radius:2px;color:#333;font-size:8.4px;display:flex;align-items:center;justify-content:center;gap:4px;box-shadow:0 1px 2px rgba(0,0,0,.5)}
.viewall svg{width:9px;height:7px;fill:#888}

/* footer */
.footer{left:0;top:1149px;width:741px;height:51px;background:var(--footer)}
.footnav{left:33px;top:1160px;font-size:8.4px;color:#bbb;display:flex;gap:7px}
.footnav .sep{color:#666}
.copy{left:33px;top:1177px;font-size:8px;color:#888}
.donate{left:508px;top:1165px;width:203px;height:23px;background:#c8302a;border-radius:3px;display:flex;align-items:center;padding:0 6px;gap:6px;font-size:8.4px;color:var(--white)}
.donate .amt{width:79px;height:14px;background:var(--white);color:#888;font-style:italic;font-size:7.5px;padding:2px 5px;border-radius:2px}
.donate .go{width:24px;height:14px;background:#f2b418;color:#5a3a00;font-weight:700;font-size:8px;display:flex;align-items:center;justify-content:center;border-radius:2px}
</style>
</head>
<body>

<header>
  <div class="abs topbar"></div>
  <div class="abs social-signin"><span class="sq"></span>sign in with Chatterly</div>
  <nav class="abs toplinks"><span>Register</span><span class="sep">|</span><span>Log in</span><span class="sep">|</span><span>Contact</span></nav>
  <div class="abs search">Search</div>

  <div class="abs brand-name">Dale Penrose</div>

  <nav class="abs mainnav" aria-label="Main">
    <svg viewBox="0 0 20 20" aria-label="Home"><path d="M10 2 1 10h3v8h4v-5h4v5h4v-8h3z"/></svg>
    <svg viewBox="0 0 20 20" aria-label="About"><circle cx="10" cy="6" r="4"/><path d="M2 18c0-5 4-7 8-7s8 2 8 7z"/></svg>
    <svg viewBox="0 0 20 20" aria-label="Notes"><path d="M2 3h16v10H8l-4 4v-4H2z"/></svg>
    <svg viewBox="0 0 20 20" aria-label="Audio"><path d="M2 7h4l5-4v14l-5-4H2z"/><path d="M13 6q3 4 0 8M15 4q5 6 0 12" stroke="#e6e6e6" stroke-width="1.6" fill="none"/></svg>
    <svg viewBox="0 0 20 20" aria-label="Video"><path d="M2 7h12v9H2z"/><path d="M14 10l5-3v9l-5-3z"/><path d="M3 6l10-3 .6 2L3.6 8z"/></svg>
    <svg viewBox="0 0 20 20" aria-label="Donations"><text x="10" y="17" text-anchor="middle" font-size="19" font-weight="700" font-family="Source Sans 3, sans-serif">$</text></svg>
    <svg viewBox="0 0 20 20" aria-label="Contact"><path d="M1 7q9-6 18 0l-2 3-3-1V7q-4-1-8 0v2l-3 1zM4 11h12l2 6H2z"/><circle cx="10" cy="14" r="2" fill="#232323"/></svg>
  </nav>
</header>

<section>
  <div class="abs band"></div>
  <div class="abs slider-frame"></div>
  <div class="abs slider"></div>
  <div class="abs slider-art" role="img" aria-label="Grey 3D figure sitting on a bench beside a large question mark"></div>
  <div class="abs steps"><span class="ask">ASK</span><span class="rec">RECEIVE</span><span class="ach">ACHIEVE</span></div>
  <div class="abs dots"><i></i><i class="on"></i><i></i><i></i><i></i></div>
  <svg class="abs arrow" style="left:39px" viewBox="0 0 18 28"><path d="M14 3 4 14l10 11"/></svg>
  <svg class="abs arrow" style="left:686px" viewBox="0 0 18 28"><path d="M4 3l10 11L4 25"/></svg>
</section>

<section class="abs intro">
  <h2>How it works</h2>
  <p>Feeling stuck? Sometimes life throws you an unexpected curve. You could speak to your friends and family, but they do not necessarily have the skills or objectivity to provide you with the help that you need to move effectively forward.</p>
  <p>Consider a trusted resource—an expert in problem solving.As a professional life strategist and business consultant, Dale Penrose has been effectively advising individuals and corporations for over 20 years.</p>
  <p>The process is simple.</p>
  <ol>
    <li>1. Register or log-in (you may use a screen name if you wish to remain anonymous).</li>
    <li>2. Select the appropriate category from the list provided.</li>
    <li>3. Post your question.</li>
    <li>4. Await Dale's response (all responses will be posted within 24 hours).</li>
    <li>5. Make your donation based on your budget/satisfaction.</li>
  </ol>
  <p class="aside">Personalized solutions in the privacy and comfort of your home…</p>
  <p class="guarantee">Satisfaction and confidentiality are guaranteed.</p>
</section>
<div class="abs portrait" role="img" aria-label="Black and white portrait of Dale reading a book"></div>

<section>
  <h2 class="abs q-title">Enter your Question</h2>
  <div class="abs q-panel"></div>
  <div class="abs q-label">Select Category :</div>
  <div class="abs q-select">Relationship<svg viewBox="0 0 8 5"><path d="M0 0h8L4 5z"/></svg></div>
  <div class="abs btn" style="left:59px;top:691px;width:47px">SIGN IN</div>
  <div class="abs btn" style="left:111px;top:691px;width:61px">REGISTER</div>
  <div class="abs q-divider"></div>
  <div class="abs q-text">What would you like to ask?</div>
  <div class="abs btn" style="left:623px;top:684px;width:61px">CONTINUE</div>
</section>

<section>
  <div class="abs cat-head" style="left:34px;top:748px"><div class="cat-icon" role="img" aria-label="Two people icon" style="background:linear-gradient(#d8b070,#6a8ab0)"></div><h3>Relationships</h3></div>
  <div class="abs cat-head" style="left:265px;top:748px"><div class="cat-icon" role="img" aria-label="Green cross icon" style="background:linear-gradient(#9ad82a,#5a9a10)"></div><h3>Health/Body</h3></div>
  <div class="abs cat-head" style="left:496px;top:748px"><div class="cat-icon" role="img" aria-label="Briefcase icon" style="background:linear-gradient(#d07a30,#8a4a18)"></div><h3>Career/Work Life</h3></div>

  <article class="abs card" style="left:34px;top:785px"><p class="lead">Neque porro quisquam est, qui dolorem ipsum quia dolor sit amet, consectetur</p><p class="body">Sed quia non numquam eius modi tempora incidunt ut labore et dolore magnam aliquam quaerat voluptatem. Ut enim ad minima veniam, quis nostrum exercitationem ullam corporis suscipit labo-riosam voluptate velit esse...</p></article>
  <article class="abs card" style="left:265px;top:785px"><p class="lead">Neque porro quisquam est, qui dolorem ipsum quia dolor sit amet, consectetur</p><p class="body">Sed quia non numquam eius modi tempora incidunt ut labore et dolore magnam aliquam quaerat voluptatem. Ut enim ad minima veniam, quis nostrum exercitationem ullam corporis suscipit labo-riosam voluptate velit esse...</p></article>
  <article class="abs card" style="left:496px;top:785px"><p class="lead">Neque porro quisquam est, qui dolorem ipsum quia dolor sit amet, consectetur</p><p class="body">Sed quia non numquam eius modi tempora incidunt ut labore et dolore magnam aliquam quaerat voluptatem. Ut enim ad minima veniam, quis nostrum exercitationem ullam corporis suscipit labo-riosam voluptate velit esse...</p></article>

  <div class="abs viewall" style="left:168px;top:909px">View all posts<svg viewBox="0 0 9 7"><path d="M0 2h5V0l4 3.5L5 7V5H0z"/></svg></div>
  <div class="abs viewall" style="left:399px;top:909px">View all posts<svg viewBox="0 0 9 7"><path d="M0 2h5V0l4 3.5L5 7V5H0z"/></svg></div>
  <div class="abs viewall" style="left:630px;top:909px">View all posts<svg viewBox="0 0 9 7"><path d="M0 2h5V0l4 3.5L5 7V5H0z"/></svg></div>

  <div class="abs cat-head" style="left:34px;top:953px"><div class="cat-icon" role="img" aria-label="Chapel icon" style="background:linear-gradient(#e0e0e0,#8a8a8a)"></div><h3>Spirituality</h3></div>
  <div class="abs cat-head" style="left:265px;top:953px"><div class="cat-icon" role="img" aria-label="Dollar sign icon" style="background:linear-gradient(#4ac0e0,#1a7aa0)"></div><h3>Money/Finance</h3></div>
  <div class="abs cat-head" style="left:496px;top:953px"><div class="cat-icon" role="img" aria-label="Envelope icon" style="background:linear-gradient(#9ac8e8,#4a7aa8)"></div><h3>Other</h3></div>

  <article class="abs card" style="left:34px;top:991px"><p class="lead">Neque porro quisquam est, qui dolorem ipsum quia dolor sit amet, consectetur</p><p class="body">Sed quia non numquam eius modi tempora incidunt ut labore et dolore magnam aliquam quaerat voluptatem. Ut enim ad minima veniam, quis nostrum exercitationem ullam corporis suscipit labo-riosam voluptate velit esse...</p></article>
  <article class="abs card" style="left:265px;top:991px"><p class="lead">Neque porro quisquam est, qui dolorem ipsum quia dolor sit amet, consectetur</p><p class="body">Sed quia non numquam eius modi tempora incidunt ut labore et dolore magnam aliquam quaerat voluptatem. Ut enim ad minima veniam, quis nostrum exercitationem ullam corporis suscipit labo-riosam voluptate velit esse...</p></article>
  <article class="abs card" style="left:496px;top:991px"><p class="lead">Neque porro quisquam est, qui dolorem ipsum quia dolor sit amet, consectetur</p><p class="body">Sed quia non numquam eius modi tempora incidunt ut labore et dolore magnam aliquam quaerat voluptatem. Ut enim ad minima veniam, quis nostrum exercitationem ullam corporis suscipit labo-riosam voluptate velit esse...</p></article>

  <div class="abs viewall" style="left:168px;top:1114px">View all posts<svg viewBox="0 0 9 7"><path d="M0 2h5V0l4 3.5L5 7V5H0z"/></svg></div>
  <div class="abs viewall" style="left:399px;top:1114px">View all posts<svg viewBox="0 0 9 7"><path d="M0 2h5V0l4 3.5L5 7V5H0z"/></svg></div>
  <div class="abs viewall" style="left:630px;top:1114px">View all posts<svg viewBox="0 0 9 7"><path d="M0 2h5V0l4 3.5L5 7V5H0z"/></svg></div>
</section>

<footer>
  <div class="abs footer"></div>
  <nav class="abs footnav"><span>Home</span><span class="sep">|</span><span>About Dale</span><span class="sep">|</span><span>Dale's Notes</span><span class="sep">|</span><span>Audio / Video</span><span class="sep">|</span><span>Donations</span><span class="sep">|</span><span>Contact Dale</span></nav>
  <div class="abs copy">Copyright © 2012 www.quizdalepenrose.com &nbsp;All rights reserved.</div>
  <div class="abs donate"><span>Click here for Donate</span><span class="amt">Select amount</span><span class="go">GO</span></div>
</footer>

</body>
</html>
```